A business card design for a dental office. We have Two doctors working here. We practice general de

I already have a logo designed for the office with the name and a slogan.
Now I need to create design for a business card using the same logo.
Details Needed on the front side of the card are :
Gerald K. Voskamp, DDS
Marvin R Duchene, DDS
418 Birchwood Lane
Portland, CT 06591
Phone : 860 517 4093
Fax : 860 517 4094
Website : WWW.BrightArcDental.Com
Office hours by appointment
On the back side of the card need :
Appointment
Date....................Time...................
With....................................
If unable to keep your appointment, please give 24-48 hours notice in order to avoid broken appointment fee.

Industry/Entity Type

Dental Clinic

Contact Information for Business Card

Gerald K. Voskamp, DDS
Marvin R Duchene, DDS
418 Birchwood Lane
Portland, CT 06591
Phone : 860 517 4093
Fax : 860 517 4094
Appointment

Requirements
Must have
• Keep the Name and slogan on the logo on the front of the card. You can move them around the Logo and Name/Slogan of business (Voskamp Family Dentistry/We give you reasons to smile) as you wish to get a feel of the design.
• Gerald K. Voskamp, DDS
• Marvin R Duchene, DDS
• 418 Birchwood Lane
• Portland, CT 06591
• Phone : 860 517 4093
• Fax : 860 517 4094
• WWW.BrightArcDental.Com
• Keep these three groups above as they are together now in different areas of the front side.
• On the back side of the card need :
• Appointment
• Date....................Time...................
• With....................................
• If unable to keep your appointment, please give 24-48 hours notice in order to avoid broken appointment fee.

```html
<!DOCTYPE html>
<html lang="en">
<head>
<meta charset="utf-8">
<title>Voskamp Family Dentistry – Business Cards</title>
<link rel="stylesheet" href="https://fonts.googleapis.com/css2?family=Raleway:ital,wght@0,400;0,500;0,600;0,700;1,400&display=swap">
<style>
  :root {
    --teal: #00a98f;
    --blue: #2b5ba8;
    --ink: #2a55a0;
    --red: #e0393e;
    --white: #ffffff;
    --page: #e9e4dc;
    --rule: #5a80bd;
    --logo-fill: #dbe7f3;
    --faint-fill: #eef2f8;
    --faint-ink: #d3dded;
  }
  * { margin: 0; padding: 0; box-sizing: border-box; }
  html, body { width: 1200px; height: 782px; overflow: hidden; }
  body {
    background: var(--page);
    font-family: "Raleway", sans-serif;
    position: relative;
  }
  .card {
    position: absolute;
    width: 527px;
    overflow: hidden;
    background: var(--white);
    box-shadow: 0 2px 5px rgba(0,0,0,.18);
  }
  .card--front { height: 311px; top: 71px; }
  .card--back  { height: 316px; top: 434px; }
  .card--front.card--single { left: 58px; }
  .card--front.card--duo    { left: 625px; top: 70px; height: 310px; }
  .card--back.card--single  { left: 61px; }
  .card--back.card--duo     { left: 625px; }

  /* front */
  .band-top { position: absolute; left: 0; top: 0; width: 100%; height: 100px; background: var(--teal); }
  .band-mid { position: absolute; left: 0; top: 100px; width: 100%; height: 62px; background: var(--white); }
  .band-low { position: absolute; left: 0; top: 162px; width: 100%; height: 149px; background: var(--blue); }
  .emblem { position: absolute; left: 0; top: 0; width: 240px; height: 311px; }
  .doctors {
    position: absolute; right: 28px; top: 54px;
    text-align: right; color: var(--white);
    font-weight: 700; font-variant: small-caps; font-size: 19px;
    letter-spacing: .5px; line-height: 24px;
  }
  .card--duo .doctors { top: 41px; }
  .practice-name {
    position: absolute; right: 28px; top: 110px;
    color: var(--ink); font-weight: 600; font-size: 21px; letter-spacing: 1px;
    text-transform: uppercase; line-height: 24px;
  }
  .slogan {
    position: absolute; right: 68px; top: 140px;
    color: var(--red); font-size: 8.5px; font-weight: 700; letter-spacing: 1.5px;
    text-transform: uppercase; display: flex; align-items: center; gap: 5px;
  }
  .slogan::before, .slogan::after { content: ""; width: 28px; height: 1px; background: var(--red); }
  .contact {
    position: absolute; right: 30px; top: 180px;
    list-style: none; color: var(--white); font-size: 14.5px; text-align: right;
    line-height: 20px;
  }
  .contact li { display: flex; justify-content: flex-end; align-items: center; gap: 4px; }
  .contact svg { width: 13px; height: 14px; fill: var(--white); }
  .hours {
    position: absolute; left: 36px; top: 267px;
    color: var(--white); font-style: italic; font-size: 14px;
  }

  /* back */
  .back-band { position: absolute; left: 0; top: 0; width: 100%; height: 75px; background: var(--teal); }
  .back-emblem { position: absolute; left: 19px; top: 8px; width: 110px; height: 110px; }
  .back-title {
    position: absolute; left: 0; width: 100%; padding-left: 42px; top: 43px;
    text-align: center; color: var(--white); font-weight: 700; font-size: 17px;
  }
  .faint-name { position: absolute; left: 363px; top: 118px; width: 160px; height: 196px; }
  .fields { position: absolute; left: 125px; top: 69px; list-style: none; width: 285px; }
  .fields li {
    display: flex; align-items: flex-end; height: 44px; color: var(--ink); font-size: 15px;
  }
  .fields .line { flex: 1; border-bottom: 1px solid var(--rule); height: 14px; margin-left: 6px; }
  .note {
    position: absolute; left: 27px; top: 264px; width: 380px;
    color: var(--ink); font-style: italic; font-size: 13.5px; line-height: 17px;
  }
</style>
</head>
<body>

<!-- Front, single doctor -->
<section class="card card--front card--single">
  <div class="band-top"></div>
  <div class="band-mid"></div>
  <div class="band-low"></div>
  <svg class="emblem" viewBox="0 0 240 311" role="img" aria-label="Voskamp Family Dentistry name mark">
    <circle cx="106" cy="130" r="116" fill="var(--white)"/>
    <path d="M -10 130 A 116 116 0 0 1 218 100" fill="none" stroke="var(--blue)" stroke-width="6"/>
    <path d="M 217.5 162 A 116 116 0 0 1 30 218" fill="none" stroke="var(--teal)" stroke-width="6"/>
    <circle cx="102" cy="125" r="56" fill="var(--logo-fill)"/>
    <text x="102" y="131" text-anchor="middle" font-family="Raleway, sans-serif" font-weight="700" font-size="17" fill="var(--ink)">Voskamp</text>
  </svg>
  <div class="doctors">Gerald K. Voskamp, DDS</div>
  <div class="practice-name">Voskamp Family Dentistry</div>
  <div class="slogan">We give you reasons to smile</div>
  <ul class="contact">
    <li><svg viewBox="0 0 12 16"><path d="M6 0a6 6 0 0 0-6 6c0 4.5 6 10 6 10s6-5.5 6-10a6 6 0 0 0-6-6zm0 8.5A2.5 2.5 0 1 1 6 3.5a2.5 2.5 0 0 1 0 5z"/></svg>418 Birchwood Lane Portland, CT 06591</li>
    <li><svg viewBox="0 0 16 16"><path d="M3.5 1l2.5 3-1.5 2c1 2 3 4 5 5l2-1.5 3 2.5-1.5 2.5C7 15 1 9 1 2.5z"/></svg>860 517 4093</li>
    <li><svg viewBox="0 0 16 16"><path d="M4 1h8v4H4zM1 6h14v8H1zm3 5h8v2H4z"/></svg>860 517 4094</li>
    <li><svg viewBox="0 0 16 16"><path d="M8 1a7 7 0 1 0 0 14A7 7 0 0 0 8 1zm0 1.5c1 1.2 1.6 3 1.7 4.8H6.3C6.4 5.5 7 3.7 8 2.5zM2.6 7.3a5.5 5.5 0 0 1 2.6-4.2 9 9 0 0 0-.9 4.2zm0 1.4h1.7c.1 1.5.4 3 .9 4.2a5.5 5.5 0 0 1-2.6-4.2zm5.4 4.8c-1-1.2-1.6-3-1.7-4.8h3.4c-.1 1.8-.7 3.6-1.7 4.8zm2.8-.6c.5-1.2.8-2.7.9-4.2h1.7a5.5 5.5 0 0 1-2.6 4.2zm.9-5.6c-.1-1.5-.4-3-.9-4.2a5.5 5.5 0 0 1 2.6 4.2z"/></svg>www.BrightArcDental.com</li>
  </ul>
  <div class="hours">Office hours by appointment</div>
</section>

<!-- Front, two doctors -->
<section class="card card--front card--duo">
  <div class="band-top"></div>
  <div class="band-mid"></div>
  <div class="band-low"></div>
  <svg class="emblem" viewBox="0 0 240 311" role="img" aria-label="Voskamp Family Dentistry name mark">
    <circle cx="106" cy="130" r="116" fill="var(--white)"/>
    <path d="M -10 130 A 116 116 0 0 1 218 100" fill="none" stroke="var(--blue)" stroke-width="6"/>
    <path d="M 217.5 162 A 116 116 0 0 1 30 218" fill="none" stroke="var(--teal)" stroke-width="6"/>
    <circle cx="102" cy="125" r="56" fill="var(--logo-fill)"/>
    <text x="102" y="131" text-anchor="middle" font-family="Raleway, sans-serif" font-weight="700" font-size="17" fill="var(--ink)">Voskamp</text>
  </svg>
  <div class="doctors">Gerald K. Voskamp, DDS<br>Marvin R Duchene, DDS</div>
  <div class="practice-name">Voskamp Family Dentistry</div>
  <div class="slogan">We give you reasons to smile</div>
  <ul class="contact">
    <li><svg viewBox="0 0 12 16"><path d="M6 0a6 6 0 0 0-6 6c0 4.5 6 10 6 10s6-5.5 6-10a6 6 0 0 0-6-6zm0 8.5A2.5 2.5 0 1 1 6 3.5a2.5 2.5 0 0 1 0 5z"/></svg>418 Birchwood Lane Portland, CT 06591</li>
    <li><svg viewBox="0 0 16 16"><path d="M3.5 1l2.5 3-1.5 2c1 2 3 4 5 5l2-1.5 3 2.5-1.5 2.5C7 15 1 9 1 2.5z"/></svg>860 517 4093</li>
    <li><svg viewBox="0 0 16 16"><path d="M4 1h8v4H4zM1 6h14v8H1zm3 5h8v2H4z"/></svg>860 517 4094</li>
    <li><svg viewBox="0 0 16 16"><path d="M8 1a7 7 0 1 0 0 14A7 7 0 0 0 8 1zm0 1.5c1 1.2 1.6 3 1.7 4.8H6.3C6.4 5.5 7 3.7 8 2.5zM2.6 7.3a5.5 5.5 0 0 1 2.6-4.2 9 9 0 0 0-.9 4.2zm0 1.4h1.7c.1 1.5.4 3 .9 4.2a5.5 5.5 0 0 1-2.6-4.2zm5.4 4.8c-1-1.2-1.6-3-1.7-4.8h3.4c-.1 1.8-.7 3.6-1.7 4.8zm2.8-.6c.5-1.2.8-2.7.9-4.2h1.7a5.5 5.5 0 0 1-2.6 4.2zm.9-5.6c-.1-1.5-.4-3-.9-4.2a5.5 5.5 0 0 1 2.6 4.2z"/></svg>www.BrightArcDental.com</li>
  </ul>
  <div class="hours">Office hours by appointment</div>
</section>

<!-- Back, single -->
<section class="card card--back card--single">
  <div class="back-band"></div>
  <svg class="back-emblem" viewBox="0 0 110 110" role="img" aria-label="Voskamp name mark">
    <circle cx="55" cy="55" r="50" fill="var(--white)"/>
    <circle cx="55" cy="55" r="36" fill="var(--logo-fill)"/>
    <text x="55" y="59" text-anchor="middle" font-family="Raleway, sans-serif" font-weight="700" font-size="11" fill="var(--ink)">Voskamp</text>
  </svg>
  <div class="back-title">Appointment:</div>
  <svg class="faint-name" viewBox="0 0 160 196" role="img" aria-label="Faint Voskamp name mark">
    <circle cx="80" cy="98" r="78" fill="var(--faint-fill)"/>
    <text x="80" y="105" text-anchor="middle" font-family="Raleway, sans-serif" font-weight="700" font-size="20" fill="var(--faint-ink)">Voskamp</text>
  </svg>
  <ul class="fields">
    <li>For <span class="line"></span></li>
    <li>Date <span class="line"></span></li>
    <li>Time <span class="line"></span></li>
    <li>With <span class="line"></span></li>
  </ul>
  <p class="note">If unable to keep your appointment, please give 24-48 hours notice in order to avoid broken appointment fee.</p>
</section>

<!-- Back, two doctors -->
<section class="card card--back card--duo">
  <div class="back-band"></div>
  <svg class="back-emblem" viewBox="0 0 110 110" role="img" aria-label="Voskamp name mark">
    <circle cx="55" cy="55" r="50" fill="var(--white)"/>
    <circle cx="55" cy="55" r="36" fill="var(--logo-fill)"/>
    <text x="55" y="59" text-anchor="middle" font-family="Raleway, sans-serif" font-weight="700" font-size="11" fill="var(--ink)">Voskamp</text>
  </svg>
  <div class="back-title">Appointment:</div>
  <svg class="faint-name" viewBox="0 0 160 196" role="img" aria-label="Faint Voskamp name mark">
    <circle cx="80" cy="98" r="78" fill="var(--faint-fill)"/>
    <text x="80" y="105" text-anchor="middle" font-family="Raleway, sans-serif" font-weight="700" font-size="20" fill="var(--faint-ink)">Voskamp</text>
  </svg>
  <ul class="fields">
    <li>For <span class="line"></span></li>
    <li>Date <span class="line"></span></li>
    <li>Time <span class="line"></span></li>
    <li>With <span class="line"></span></li>
  </ul>
  <p class="note">If unable to keep your appointment, please give 24-48 hours notice in order to avoid broken appointment fee.</p>
</section>

</body>
</html>
```